business card with logo

Would like a business card for an electrical contractor called BRANLOCK ELECTRICS.
No generic electrical imagery (light globe, powerpoints, ect). Would like a logo or symbol created in the design as part of the project . I would like crisp colour. No templated designs like Printvox

is there any other designers willing to submit designs

Electrical

```html
<!DOCTYPE html>
<html lang="en">
<head>
<meta charset="utf-8">
<title>Branlock Electrics – Business Card</title>
<link rel="stylesheet" href="https://fonts.googleapis.com/css2?family=Cinzel:wght@400&family=Montserrat:wght@600&family=Quicksand:wght@400&display=swap">
<style>
  :root {
    --backdrop: #e9e7e3;
    --card-black: #231f20;
    --navy: #2c3a85;
    --royal: #3b55a8;
    --steel: #8a8b8f;
    --paper-light: #fbfbfb;
    --paper-edge: #d9dadc;
    --white: #ffffff;
  }
  * { box-sizing: border-box; margin: 0; padding: 0; }
  html, body {
    width: 1200px; height: 1000px; overflow: hidden;
    background: var(--backdrop);
  }
  .stage { position: relative; width: 1200px; height: 1000px; }

  .card {
    position: absolute;
    width: 700px; height: 400px;
    box-shadow: 0 10px 28px rgba(0,0,0,.18);
    overflow: hidden;
  }

  /* Front */
  .card--front { left: 70px; top: 70px; background: var(--card-black); }
  .front-mark {
    position: absolute; left: 0; right: 0; top: 130px;
    display: flex; align-items: center; justify-content: center; gap: 22px;
  }
  .front-mark__square { width: 26px; height: 26px; background: var(--royal); flex: none; }
  .front-mark__name {
    font-family: "Cinzel", Georgia, serif; font-weight: 400;
    font-size: 44px; letter-spacing: 4px; color: var(--royal); white-space: nowrap;
  }
  .front-band {
    position: absolute; left: 0; right: 0; top: 300px; height: 44px;
    background: linear-gradient(90deg, var(--navy) 0%, var(--navy) 45%, var(--royal) 100%);
    display: flex; align-items: center; justify-content: center;
  }
  .front-band__url {
    font-family: "Quicksand", Arial, sans-serif; font-size: 22px; color: var(--white);
  }

  /* Back */
  .card--back {
    left: 430px; top: 530px;
    background: radial-gradient(ellipse at 55% 55%, var(--white) 0%, var(--paper-light) 30%, var(--paper-edge) 100%);
  }
  .back-name {
    position: absolute; left: 40px; top: 36px;
    font-family: "Montserrat", Arial, sans-serif; font-weight: 600;
    font-size: 38px; color: var(--navy); letter-spacing: .5px; white-space: nowrap;
  }
  .contact {
    position: absolute; right: 44px; top: 210px; text-align: right;
  }
  .contact__person {
    font-family: "Montserrat", Arial, sans-serif; font-weight: 600;
    font-size: 27px; color: var(--navy); margin-bottom: 10px;
  }
  .contact__line {
    display: flex; align-items: center; justify-content: flex-end; gap: 8px;
    font-family: "Quicksand", Arial, sans-serif; font-size: 22px;
    color: var(--steel); line-height: 32px; white-space: nowrap;
  }
  .contact__icon { width: 18px; height: 18px; flex: none; }
  .contact__line--plain { padding-right: 26px; }
  .back-band {
    position: absolute; left: 0; right: 0; bottom: 0; height: 34px;
    background: linear-gradient(90deg, var(--navy) 0%, var(--royal) 50%, var(--navy) 100%);
  }
</style>
</head>
<body>
<main class="stage">
  <section class="card card--front">
    <div class="front-mark">
      <span class="front-mark__square"></span>
      <span class="front-mark__name">BRANLOCK ELECTRICS</span>
    </div>
    <div class="front-band">
      <span class="front-band__url">www.branlockelectrics.com</span>
    </div>
  </section>

  <section class="card card--back">
    <h1 class="back-name">BRANLOCK ELECTRICS</h1>
    <div class="contact">
      <p class="contact__person">MARCUS HALE</p>
      <p class="contact__line">0491 827 365
        <svg class="contact__icon" viewBox="0 0 18 18" aria-hidden="true">
          <rect x="5" y="1" width="8" height="16" rx="1.5" fill="none" stroke="#2c3a85" stroke-width="1.6"/>
          <line x1="8" y1="14.5" x2="10" y2="14.5" stroke="#2c3a85" stroke-width="1.4"/>
        </svg>
      </p>
      <p class="contact__line">branlockelec@mailpost.com
        <svg class="contact__icon" viewBox="0 0 18 18" aria-hidden="true">
          <rect x="1" y="4" width="16" height="11" fill="none" stroke="#2c3a85" stroke-width="1.6"/>
          <polyline points="1,4 9,10.5 17,4" fill="none" stroke="#2c3a85" stroke-width="1.6"/>
        </svg>
      </p>
      <p class="contact__line contact__line--plain">rec#40583</p>
    </div>
    <div class="back-band"></div>
  </section>
</main>
</body>
</html>
```